Scrap Metal Recycling

We are looking for a simple yet bold business card. We already have the logo, please see attached. Color scheme of blue, black and white or just blue and white.

```html
<!DOCTYPE html>
<html lang="en">
<head>
<meta charset="UTF-8">
<title>R.K. Alloys Inc. – Business Card</title>
<link href="https://fonts.googleapis.com/css2?family=Montserrat:wght@400;500;600&family=Oswald:wght@500&display=swap" rel="stylesheet">
<style>
  :root {
    --stage: #e6e7e9;
    --card-white: #ffffff;
    --card-dark: #393939;
    --ink: #3a3a3a;
    --ink-deep: #262626;
    --teal: #0b8db0;
    --white: #ffffff;
  }
  * { margin: 0; padding: 0; box-sizing: border-box; }
  html, body {
    width: 1048px; height: 1200px; overflow: hidden;
    background: var(--stage);
    font-family: "Montserrat", sans-serif;
  }
  .canvas { position: relative; width: 1048px; height: 1200px; }

  .card { position: absolute; width: 843px; height: 482px; }
  .card--front { left: 84px; top: 87px; background: var(--card-white); }
  .card--back { left: 77px; top: 623px; background: var(--card-dark); }

  .brand-name {
    position: absolute; left: 0; right: 0; text-align: center;
    font-weight: 600; font-size: 62px; letter-spacing: -1px; line-height: 1;
  }
  .brand-tagline {
    position: absolute; left: 0; right: 0; text-align: center;
    font-weight: 600; font-size: 27px; letter-spacing: 11px; line-height: 1;
  }
  .card--front .brand-name { top: 112px; color: var(--ink); }
  .card--front .brand-tagline { top: 184px; color: var(--teal); }
  .card--back .brand-name { top: 200px; color: var(--ink-deep); }
  .card--back .brand-tagline { top: 277px; color: var(--ink-deep); }

  .person { position: absolute; left: 146px; top: 267px; text-align: right; }
  .person__name {
    font-family: "Oswald", sans-serif; font-weight: 500;
    font-size: 40px; line-height: 1; color: var(--teal); letter-spacing: -1px;
  }
  .person__role { margin-top: 8px; font-size: 22px; color: var(--ink); }

  .divider {
    position: absolute; left: 392px; top: 264px; width: 2px; height: 82px;
    background: var(--teal);
  }

  .contacts { position: absolute; left: 414px; top: 263px; list-style: none; }
  .contacts li {
    display: flex; align-items: center; gap: 12px;
    font-size: 22px; color: var(--ink); height: 31px;
  }
  .contacts svg { width: 20px; height: 20px; flex: none; fill: var(--teal); }

  .address-band {
    position: absolute; left: -3px; right: -3px; top: 388px; height: 34px;
    background: var(--teal); color: var(--white);
    font-size: 21px; display: flex; align-items: center; justify-content: center;
  }
</style>
</head>
<body>
<main class="canvas">
  <section class="card card--front">
    <h1 class="brand-name">R.K. ALLOYS INC.</h1>
    <p class="brand-tagline">SCRAP METAL RECYCLING</p>

    <div class="person">
      <p class="person__name">DANIEL REYES</p>
      <p class="person__role">Managing Director</p>
    </div>

    <span class="divider"></span>

    <ul class="contacts">
      <li>
        <svg viewBox="0 0 24 24" aria-hidden="true"><path d="M6.6 10.8a15 15 0 0 0 6.6 6.6l2.2-2.2a1 1 0 0 1 1-.25 11.4 11.4 0 0 0 3.6.57 1 1 0 0 1 1 1V20a1 1 0 0 1-1 1A17 17 0 0 1 3 4a1 1 0 0 1 1-1h3.5a1 1 0 0 1 1 1c0 1.25.2 2.45.57 3.57a1 1 0 0 1-.25 1z"/></svg>
        044-987 654 321
      </li>
      <li>
        <svg viewBox="0 0 24 24" aria-hidden="true"><path d="M2 5h20v14H2z M4 7v.4l8 5.6 8-5.6V7z" fill-rule="evenodd"/></svg>
        hello@rkalloys.com
      </li>
      <li>
        <svg viewBox="0 0 24 24" aria-hidden="true"><circle cx="12" cy="12" r="10"/><path d="M2 12h20M12 2c3 3 3 17 0 20M12 2c-3 3-3 17 0 20" stroke="#fff" stroke-width="1.4" fill="none"/></svg>
        www.rkalloys.com
      </li>
    </ul>

    <div class="address-band">87, Harbor Road West&nbsp; Country Name, 30218</div>
  </section>

  <section class="card card--back">
    <p class="brand-name">R.K. ALLOYS INC.</p>
    <p class="brand-tagline">SCRAP METAL RECYCLING</p>
  </section>
</main>
</body>
</html>
```